We need a Welcome Booklet designed for our Church - Larkspur Commons Fellowship. We would like a design that is contemporary with no religious symbols or old pictures. Please use quality contemporary photos . See attached a Word document with what content we want in the booklet.

Target Market(s)

Guests to the church so new person friendly

Requirements
Must have
• A contemporary modern look
Should not have
• Religious symbols or old pictures

```html
<!DOCTYPE html>
<html lang="en">
<head>
<meta charset="utf-8">
<title>Vision – Larkspur Commons Fellowship</title>
<link rel="stylesheet" href="https://fonts.googleapis.com/css2?family=Questrial&family=Source+Serif+4:wght@400&family=Mulish:ital,wght@1,800&display=swap">
<style>
  :root {
    --ink: #1d1d1f;
    --paper: #ffffff;
    --vision-green: #3f7a12;
    --pillar-lime: #8fe01a;
    --header-deep: #0b1c33;
    --header-blue: #1f4f82;
    --brand-blue: #1f6fb0;
    --sky-top: #e9dcc0;
    --sky-cloud: #b9c4cf;
    --rock: #2b2f2e;
    --room-warm: #7d7266;
    --room-cool: #3c4a55;
  }
  * { margin: 0; padding: 0; box-sizing: border-box; }
  html, body { width: 855px; height: 1200px; overflow: hidden; background: var(--paper); }
  .page {
    position: relative;
    width: 855px; height: 1200px;
    background: var(--paper);
    color: var(--ink);
    font-family: "Questrial", "Century Gothic", sans-serif;
    font-size: 21px;
    line-height: 28px;
  }
  .hero {
    position: absolute; left: 0; top: 0; width: 855px; height: 203px;
    background:
      radial-gradient(ellipse at 45% 40%, rgba(70,130,190,0.55), transparent 60%),
      linear-gradient(180deg, var(--header-blue) 0%, var(--header-deep) 100%);
  }
  .hero-title {
    position: absolute; left: 61px; top: 110px;
    font-family: "Source Serif 4", Georgia, serif;
    font-weight: 400; font-size: 46px; line-height: 52px;
    color: var(--paper);
  }
  .block { position: absolute; }
  .vision-line { left: 58px; top: 244px; }
  .vision-line em {
    font-family: "Mulish", "Century Gothic", sans-serif;
    font-style: italic; font-weight: 800; color: var(--vision-green);
  }
  .purpose { left: 58px; top: 302px; }
  .pillars { left: 92px; top: 371px; list-style: none; }
  .pillars li { height: 43px; }
  .pillars b {
    font-family: "Mulish", "Century Gothic", sans-serif;
    font-style: italic; font-weight: 800; color: var(--pillar-lime);
  }
  .family {
    left: 60px; top: 584px; width: 730px;
    text-align: justify; hyphens: auto;
  }
  .beliefs { left: 57px; top: 733px; width: 740px; }
  .network { left: 60px; top: 840px; width: 400px; text-align: justify; }
  .photo { position: absolute; }
  .photo-summit {
    left: 517px; top: 838px; width: 268px; height: 266px;
    background:
      linear-gradient(180deg, var(--sky-top) 0%, #cfd3d4 14%, var(--sky-cloud) 40%, #7d8b95 62%, var(--rock) 82%, #1a1c1b 100%);
  }
  .photo-gathering {
    left: 246px; top: 957px; width: 330px; height: 183px;
    border-left: 4px solid var(--paper); border-top: 4px solid var(--paper);
    background: linear-gradient(120deg, var(--room-warm) 0%, #9a8e7e 40%, var(--room-cool) 100%);
  }
  .brand {
    position: absolute; left: 42px; top: 1078px;
    display: flex; align-items: center; gap: 10px;
    font-family: "Questrial", "Century Gothic", sans-serif;
    font-size: 30px; color: var(--brand-blue);
  }
  .brand-dot { width: 16px; height: 16px; border-radius: 50%; background: var(--brand-blue); }
</style>
</head>
<body>
<main class="page">
  <header class="hero" role="img" aria-label="Photo of a worship team singing on stage under blue lighting">
    <h1 class="hero-title">Vision</h1>
  </header>

  <p class="block vision-line">Our vision is <em>Transformed Lives Transforming Lives</em></p>
  <p class="block purpose">We believe that God has uniquely created us for His good purposes.</p>

  <ul class="block pillars">
    <li><b>BUILD</b>…..Healthy lives</li>
    <li><b>BELONG</b>…..to your church and community</li>
    <li><b>BECOME</b>….. Know your Gift &amp; Role</li>
    <li><b>BE-ASSIGNED</b>…..to Change your World</li>
  </ul>

  <p class="block family">Larkspur Commons Fellowship is a part of the Harbourline Alliance family of churches that has 450 churches nationwide and a Harbourline global family of international works and outreaches. We have a theological training centre: Ashbury Ministry College.</p>

  <p class="block beliefs">Our key beliefs are that Jesus can Save us, Heal us, Fill us, and Jesus will bring history to the best conclusion on His return.</p>

  <p class="block network">We are networked across our City and have a deep passion for unity and churches working together</p>

  <div class="photo photo-summit" role="img" aria-label="Photo of a person sitting on a mountain summit above a sea of clouds"></div>
  <div class="photo photo-gathering" role="img" aria-label="Photo of a small group listening to a speaker in a bright room"></div>

  <div class="brand"><span class="brand-dot"></span><span>Harbourline</span></div>
</main>
</body>
</html>
```